Health - Still Meadow Project

I am running a new Still Meadow Conference that will have meditation, mediums and healers - this is a first time conference. However the conference is aimed at mainstream 'normal' people. The 'normal' people, don't want to hear or see words like Tantra, Prana, Angels, etc, but they have problems that can be alleviated through these mediums. The design should communicate light, soothing, comforting, healing. I would like a web design for a single page that can be used as a landing page for the conference registration. I also need a logo and a flyer that can be made into posters A4 or A3 posters. I need to be able to edit all documents as there will be changes in the program through time. I have attached the initial agenda. This conference will be held in Victoria, Australia.
Target Market(s)
Mums and grandmas
Industry/Entity Type
Health And Wellness
Number of Pages Required
1 page

```html
<!DOCTYPE html>
<html lang="en">
<head>
<meta charset="utf-8">
<title>Still Meadow Conference</title>
<link href="https://fonts.googleapis.com/css2?family=Lobster&family=Open+Sans:wght@400;600;700&family=Raleway:wght@400;500;600&display=swap" rel="stylesheet">
<style>
:root{
  --teal:#1bb99a;
  --teal-dark:#159e83;
  --ink:#2b2b2b;
  --body:#555;
  --line:#e4e4e4;
  --band:#f1f1f1;
  --footer:#3a3a3a;
  --footer-deep:#2a2a2a;
  --white:#fff;
}
*{box-sizing:border-box;margin:0;padding:0}
html,body{width:1200px;height:2329px;overflow:hidden}
body{position:relative;background:var(--white);font-family:"Open Sans",sans-serif;color:var(--body)}
.abs{position:absolute}

/* hero */
.hero{left:0;top:0;width:1200px;height:528px;background:linear-gradient(100deg,#8a6a55 0%,#c9a58e 28%,#e9d6c8 45%,#b9a489 62%,#6f7560 80%,#8d9a7c 100%)}
.logo{left:93px;top:38px;font-family:"Lobster",sans-serif;font-size:27px;color:var(--teal)}
.hero-title{right:98px;top:78px;font-family:"Lobster",sans-serif;font-size:40px;font-weight:400;color:var(--white)}
.hero-btn{left:916px;top:160px;width:183px;height:39px;background:var(--white);border:1px solid #ddd;color:var(--teal);font-size:13px;font-weight:600;display:flex;align-items:center;justify-content:center}
.hero-arrow{top:248px}

/* conference panel */
.panel{left:99px;top:436px;width:1002px;height:522px;background:var(--teal);box-shadow:0 24px 28px -18px rgba(0,0,0,.25)}
.panel-title{left:0;top:32px;width:100%;text-align:center;font-family:"Raleway",sans-serif;font-weight:400;font-size:31px;line-height:46px;color:var(--white)}
.panel-box{left:24px;top:160px;width:956px;height:312px;background:var(--white);border:1px solid #555}
.topic{top:24px;width:284px;height:262px;border:2px solid #ddd}
.topic span{position:absolute;left:22px;bottom:18px;font-family:"Raleway",sans-serif;font-size:31px;color:var(--white)}
.topic-1{left:20px;background:linear-gradient(160deg,#e8874a,#a85a5f 45%,#3e2536)}
.topic-2{left:336px;background:linear-gradient(180deg,#6d7fa8,#c6a07c 55%,#2c2a33)}
.topic-3{left:649px;background:linear-gradient(160deg,#f5d9e6,#e9c0d0 45%,#b8a3ae)}

/* speakers */
.section-title{font-family:"Raleway",sans-serif;font-weight:500;font-size:26px;color:var(--teal)}
.speakers-title{left:96px;top:1008px}
.speakers-rule{left:96px;top:1052px;width:1006px;height:1px;background:var(--line)}
.speaker{top:1195px;width:239px;height:523px;border:1px solid #ececec;text-align:center;display:flex;flex-direction:column;align-items:center;padding-top:128px}
.speaker .avatar{position:absolute;left:11px;top:-104px;width:216px;height:216px;border-radius:50%;border:3px solid #e3e3e3}
.speaker h3{font-family:"Raleway",sans-serif;font-weight:500;font-size:22px;line-height:30px;color:var(--ink)}
.speaker .time{margin-top:6px;font-size:15px;line-height:22px;font-weight:600;color:var(--teal)}
.speaker .topic-name{margin-top:6px;font-family:"Raleway",sans-serif;font-size:17px;line-height:28px;color:#333}
.speaker p{margin-top:12px;width:220px;font-size:10.6px;line-height:28px;text-align:justify;text-align-last:center;hyphens:auto;-webkit-hyphens:auto;color:#444}
.speaker .more{margin-top:4px;font-size:12px;line-height:20px;color:var(--teal)}
.s1{left:98px}.s2{left:352px}.s3{left:607px}.s4{left:862px}

/* testimonials */
.testimonials{left:0;top:1742px;width:1200px;height:268px;background:linear-gradient(135deg,#f6f6f6 0%,#ececec 50%,#f4f4f4 100%);border-top:1px solid #e2e2e2}
.testi-title{left:120px;top:30px}
.testi-rule{left:350px;top:48px;width:720px;height:1px;background:#ddd}
.testi-nav{left:1078px;top:34px;font-size:18px;color:#999;letter-spacing:2px}
.quote-circle{left:98px;top:108px;width:96px;height:96px;border-radius:50%;background:#8c8c8c}
.client-photo{left:157px;top:95px;width:122px;height:122px;border-radius:50%;border:4px solid var(--white);background:linear-gradient(160deg,#d9cfc9,#b08f7d)}
.testi-text{left:329px;top:108px;width:768px;font-size:12.5px;line-height:26px;color:#555}
.testi-author{left:329px;top:192px;font-size:15px;color:var(--teal)}

/* footer */
.footer{left:0;top:2010px;width:1200px;height:246px;background:var(--footer)}
.footer-logo{left:101px;top:106px;font-family:"Lobster",sans-serif;font-size:34px;color:var(--white)}
.f-col{top:44px;color:var(--white)}
.f-col h4{font-size:14px;font-weight:700;margin-bottom:16px}
.f-col li{list-style:none;font-size:12px;line-height:27px}
.f-col li::before{content:"»";margin-right:10px}
.f-menus{left:363px}.f-links{left:505px}.f-contact{left:699px;width:210px}.f-connect{left:922px}
.contact-row{display:flex;gap:14px;font-size:11.5px;line-height:23px;color:#ccc;margin-bottom:14px}
.contact-row svg{flex:none;margin-top:4px}
.socials{display:flex;gap:12px;margin-top:6px}
.socials span{width:37px;height:37px;border-radius:50%;border:2px solid var(--white)}
.bottom-bar{left:0;top:2256px;width:1200px;height:73px;background:var(--footer-deep);color:var(--white);font-size:12px;display:flex;align-items:center;justify-content:center;gap:8px}
</style>
</head>
<body>

<header class="hero abs" role="img" aria-label="Photo of a smiling mother holding her baby in a garden">
</header>
<div class="logo abs">Still Meadow</div>
<h1 class="hero-title abs">See Your Path to Happiness</h1>
<div class="hero-btn abs">Conference Registration</div>
<svg class="hero-arrow abs" style="left:50px" width="16" height="26" viewBox="0 0 16 26"><path d="M13 3 3 13l10 10" fill="none" stroke="#fff" stroke-width="3"/></svg>
<svg class="hero-arrow abs" style="left:1132px" width="16" height="26" viewBox="0 0 16 26"><path d="M3 3l10 10L3 23" fill="none" stroke="#fff" stroke-width="3"/></svg>

<section class="panel abs">
  <h2 class="panel-title abs">Still Meadow Conference On Saturday<br>August 20th 2016 that will have</h2>
  <div class="panel-box abs">
    <div class="topic topic-1 abs" role="img" aria-label="Photo of a person meditating in warm light"><span>Meditation</span></div>
    <div class="topic topic-2 abs" role="img" aria-label="Silhouette of a person praying at sunset by the water"><span>Mediums</span></div>
    <div class="topic topic-3 abs" role="img" aria-label="Photo of a healing session with hands above a resting woman"><span>Healers</span></div>
  </div>
</section>

<h2 class="section-title speakers-title abs">Our Speakers</h2>
<div class="speakers-rule abs"></div>

<article class="speaker s1 abs">
  <div class="avatar" role="img" aria-label="Portrait of speaker Wren Hollis" style="background:linear-gradient(160deg,#6b5a4e,#c79a86)"></div>
  <h3>Wren Hollis</h3>
  <div class="time">9:00 – 10:45</div>
  <div class="topic-name">Embarking Upon the<br>Spiritual Life</div>
  <p>Everyone is searching for love, joy and peace – aren't we? Yet love, joy and peace is already our natural state of being. So how did we come to forget this fundamental Truth? Why are we searching for what we already are? The answers to these questions are rather simple and obvious but only</p>
  <div class="more">View More &gt;&gt;</div>
</article>

<article class="speaker s2 abs">
  <div class="avatar" role="img" aria-label="Portrait of speaker Lena Maris" style="background:linear-gradient(160deg,#e4dccd,#a8785a)"></div>
  <h3>Lena Maris</h3>
  <div class="time">11:00 – 12:45</div>
  <div class="topic-name">Conscious Connection &amp;<br>Living Life Fully</div>
  <p>We live in a world where most people feel disconnected or 'out of synch' with friends, loved ones and the daily experiences we share with one another. This workshop is designed to offer you a framework for LIVING more consciously, intimately and with greater connection, presence and depth</p>
  <div class="more">View More &gt;&gt;</div>
</article>

<article class="speaker s3 abs">
  <div class="avatar" role="img" aria-label="Portrait of speaker Paul Fenwick" style="background:linear-gradient(160deg,#4f79b0,#c79c84)"></div>
  <h3>Paul Fenwick</h3>
  <div class="time">1:30 – 3:15</div>
  <div class="topic-name">The Slow Breath<br>to Freedom</div>
  <p>Stress is is one of the number one causes of leading diseases today. The connection between Mind and Body has long since been established by both science and spirituality. This session will guide you through simple meditations, self-inquiry, mindful eating and movement.</p>
  <div class="more">View More &gt;&gt;</div>
</article>

<article class="speaker s4 abs">
  <div class="avatar" role="img" aria-label="Portrait of speaker Wren Hollis outdoors" style="background:linear-gradient(160deg,#8aa06a,#c4a188)"></div>
  <h3>Wren Hollis</h3>
  <div class="time">3:30 – 5pm</div>
  <div class="topic-name">Learning to<br>SHINE</div>
  <p>In a world where too often we feel less than our bright, shiny best we can all afford to bring out more of our own natural light to shine for ourselves and others. In this session, Clara will guide you through ways to connect with your inner SHINE and not only use that to brighten</p>
</article>

<section class="testimonials abs">
  <h2 class="section-title testi-title abs">Our Testimonials</h2>
  <div class="testi-rule abs"></div>
  <div class="testi-nav abs">‹ ›</div>
  <div class="quote-circle abs">
    <svg width="96" height="96" viewBox="0 0 96 96"><g fill="#fff"><rect x="22" y="40" width="12" height="12"/><path d="M22 46q0-10 9-12v4q-5 2-5 8z"/><rect x="38" y="40" width="12" height="12"/><path d="M38 46q0-10 9-12v4q-5 2-5 8z"/></g></svg>
  </div>
  <div class="client-photo abs" role="img" aria-label="Portrait of a smiling client wearing glasses"></div>
  <p class="testi-text abs">An vero utroque duo. Nam ea illum invenire, usu dicunt euismod maluisset ea. Homero laoreet in usu, utinam vocent bonorum mel ut. Summo tempor id vix, vis ad idque omittam lucilius. Mei ex insolens inimicus. In minim dolorem qualisque sea. An vero utroque duo. Nam ea illum invenire, usu dicunt euismod maluisset ea. Homero laoreet in usu, utinam vocent bonorum mel ut.</p>
  <div class="testi-author abs">- Dicam mucius mandamus</div>
</section>

<footer class="footer abs">
  <div class="footer-logo abs">Still Meadow</div>
  <div class="f-col f-menus abs">
    <h4>MENUS</h4>
    <ul><li>Home</li><li>About us</li><li>Our services</li><li>Blog</li><li>Contact us</li></ul>
  </div>
  <div class="f-col f-links abs">
    <h4>QUICK LINKS</h4>
    <ul><li>Site map</li><li>Terms and Conditions</li><li>Disclaimer</li><li>Privacy Policy</li><li>Contact us</li></ul>
  </div>
  <div class="f-col f-contact abs">
    <h4>CONTACT US</h4>
    <div class="contact-row">
      <svg width="16" height="14" viewBox="0 0 16 14"><path d="M8 0 0 7h2v7h4V9h4v5h4V7h2z" fill="#fff"/></svg>
      <span>Fernvale Community Hall at 12 Linden Road Fernvale Victoria 3999</span>
    </div>
    <div class="contact-row">
      <svg width="16" height="18" viewBox="0 0 16 18"><rect x="4" y="1" width="8" height="16" rx="1.5" fill="none" stroke="#fff" stroke-width="1.6"/><circle cx="8" cy="14" r="1" fill="#fff"/></svg>
      <span>Call Us : (555)010-2468</span>
    </div>
    <div class="contact-row">
      <svg width="16" height="12" viewBox="0 0 16 12"><rect x="1" y="1" width="14" height="10" fill="none" stroke="#fff" stroke-width="1.4"/><path d="M1 1l7 6 7-6" fill="none" stroke="#fff" stroke-width="1.4"/></svg>
      <span>info@stillmeadow.example</span>
    </div>
  </div>
  <div class="f-col f-connect abs">
    <h4>CONNECT US WITH</h4>
    <div class="socials"><span></span><span></span><span></span><span></span></div>
  </div>
</footer>
<div class="bottom-bar abs">
  <svg width="13" height="13" viewBox="0 0 13 13"><circle cx="6.5" cy="6.5" r="5.7" fill="none" stroke="#fff" stroke-width="1.3"/><path d="M8.6 4.6a2.6 2.6 0 1 0 0 3.8" fill="none" stroke="#fff" stroke-width="1.3"/></svg>
  <span>Still Meadow 2016 . All Rights Reserved</span>
</div>

</body>
</html>
```